Business Card Design Project

Use our current logo. Clean design.

Industry/Entity Type

Business

Requirements
Must have
• Marisela DUBRANCQ
M. Law
Managing Partner

Alpenvorsa AG
Kornhalmweg 214
CH-3097 Liebefeld

M. +41 79 412 56 27
T. +41 31 928 44 10
F. +41 31 928 44 19

m.dubrancq@alpenvorsa-example.com
www.alpenvorsa-example.com

```html
<!DOCTYPE html>
<html lang="en">
<head>
<meta charset="utf-8">
<title>Alpenvorsa AG – Business Card</title>
<link rel="stylesheet" href="https://fonts.googleapis.com/css2?family=Tenor+Sans&display=swap">
<style>
  :root {
    --stage: #1b1a1a;
    --card: #2a2526;
    --ink: #f1efef;
    --ink-soft: #cfcaca;
    --rule: #8a8484;
  }
  * { box-sizing: border-box; margin: 0; padding: 0; }
  html, body {
    width: 1200px; height: 900px; overflow: hidden;
    background: var(--stage);
    font-family: "Tenor Sans", "Optima", sans-serif;
    color: var(--ink);
  }
  .stage {
    position: relative; width: 1200px; height: 900px;
    display: flex; justify-content: center; align-items: center; gap: 60px;
  }
  .card {
    position: relative; width: 320px; height: 540px;
    background: var(--card); border-radius: 30px;
    text-align: center;
  }
  .brand-name {
    letter-spacing: 0.06em; text-transform: uppercase; color: var(--ink);
  }
  /* Front */
  .card-front .brand-name {
    position: absolute; left: 0; right: 0; top: 218px; font-size: 32px;
  }
  .card-front .website {
    position: absolute; left: 0; right: 0; bottom: 86px; font-size: 14px; letter-spacing: 0.03em;
  }
  /* Back */
  .card-back { padding: 62px 36px 0; }
  .card-back .brand-name { font-size: 17px; margin-bottom: 22px; }
  .company { font-size: 15px; line-height: 1.25; }
  .address { font-size: 13px; color: var(--ink-soft); line-height: 1.25; }
  .person { margin-top: 64px; }
  .person-name { font-size: 18px; letter-spacing: 0.04em; text-transform: uppercase; }
  .person-degree, .person-role { font-size: 13px; color: var(--ink-soft); line-height: 1.2; }
  .rule { height: 1px; background: var(--rule); margin: 16px 0 14px; }
  .contact-label { font-size: 9px; letter-spacing: 0.08em; text-transform: uppercase; color: var(--ink-soft); line-height: 1.1; }
  .contact-number { font-size: 15px; line-height: 1.2; letter-spacing: 0.04em; margin-bottom: 2px; }
  .online { font-size: 14px; line-height: 1.3; }
</style>
</head>
<body>
  <main class="stage">
    <section class="card card-front" aria-label="Card front">
      <div class="brand-name">Alpenvorsa</div>
      <div class="website">www.alpenvorsa-example.com</div>
    </section>

    <section class="card card-back" aria-label="Card back">
      <div class="brand-name">Alpenvorsa</div>
      <div class="company">Alpenvorsa AG</div>
      <div class="address">Kornhalmweg 214<br>CH-3097 Liebefeld</div>

      <div class="person">
        <div class="person-name">Marisela Dubrancq</div>
        <div class="person-degree">M. Law</div>
        <div class="person-role">Managing Partner</div>
      </div>

      <div class="rule"></div>

      <div class="contact">
        <div class="contact-label">Mobile:</div>
        <div class="contact-number">+41 79 412 56 27</div>
        <div class="contact-label">Telephone:</div>
        <div class="contact-number">+41 31 928 44 10</div>
        <div class="contact-label">Fax:</div>
        <div class="contact-number">+41 31 928 44 19</div>
      </div>

      <div class="rule"></div>

      <div class="online">
        <div>m.dubrancq@alpenvorsa-example.com</div>
        <div>www.alpenvorsa-example.com</div>
      </div>

      <div class="rule"></div>
    </section>
  </main>
</body>
</html>
```